Wine Label Design for the red wine named “Amber Moth Ridge” or “A/M”

Create an elegant yet simple (less is more) label for a red, full-bodied wine from a family-owned Herzegovinian vineyard by the river with 9 names. You can use elements such as the Calopteryx virgo, possibly the river shape, and ensure a coherent storytelling of the unique vineyard’s locality and meticulous, hand-picked grape cultivation.
Let’s craft a label that is not just seen, but is experienced and remembered.

Target Market(s)

Wine lovers that appreciate high quality wines

Industry/Entity Type

Wine, Family owned small producer

Requirements
Must have
• Name A/M, front and back label. Premium feel, uniqueness. Simple but interesting.
Nice to have
• Please see the images below as an idea of various directions. I am also leaning to embossed image on the label
Should not have
• Should not be overcrowded with text, too many images and objects

```html
<!DOCTYPE html>
<html lang="en">
<head>
<meta charset="utf-8">
<title>Amber Moth Ridge – Full-Bodied Red Label</title>
<link rel="stylesheet" href="https://fonts.googleapis.com/css2?family=Roboto+Condensed:wght@400;500&family=Libre+Baskerville:wght@400&display=swap">
<style>
  :root {
    --backdrop: #1b1b1c;
    --label-ring: #2a2a2b;
    --ring-text: #c9c9cb;
    --story-text: #a6a6a9;
    --marble-light: #f4f8fb;
    --marble-mid: #c9dcea;
    --marble-deep: #8fb1cc;
    --mark-violet: #5a2a8c;
    --ink: #1d1d1f;
    --wine-red: #a3195b;
  }
  html, body {
    margin: 0;
    padding: 0;
    width: 1200px;
    height: 1200px;
    overflow: hidden;
    background: var(--backdrop);
  }
  .label-canvas {
    display: block;
    width: 1200px;
    height: 1200px;
  }
  .label-ring { fill: var(--label-ring); }
  .wine-name {
    font-family: "Roboto Condensed", "Arial Narrow", sans-serif;
    font-weight: 400;
    font-size: 60px;
    fill: var(--ring-text);
  }
  .vineyard-story {
    font-family: "Roboto Condensed", "Arial Narrow", sans-serif;
    font-weight: 400;
    font-size: 25.5px;
    fill: var(--story-text);
  }
  .brand-mark {
    font-family: "Libre Baskerville", Georgia, serif;
    font-size: 150px;
    fill: var(--mark-violet);
  }
  .wine-style {
    font-family: "Libre Baskerville", Georgia, serif;
    font-size: 30px;
    fill: var(--ink);
  }
  .wine-type {
    font-family: "Roboto Condensed", "Arial Narrow", sans-serif;
    font-weight: 400;
    font-size: 40px;
    fill: var(--wine-red);
  }
  .craft-note {
    font-family: "Roboto Condensed", "Arial Narrow", sans-serif;
    font-weight: 400;
    font-size: 22px;
    fill: var(--ink);
  }
  .craft-rule { stroke: var(--ink); stroke-width: 1.5; }
</style>
</head>
<body>
<svg class="label-canvas" viewBox="0 0 1200 1200" xmlns="http://www.w3.org/2000/svg">
  <defs>
    <radialGradient id="marble-wash" cx="50%" cy="45%" r="60%">
      <stop offset="0%" stop-color="var(--marble-light)"/>
      <stop offset="55%" stop-color="var(--marble-mid)"/>
      <stop offset="100%" stop-color="var(--marble-deep)"/>
    </radialGradient>
    <path id="title-arc" d="M190,600 A410,410 0 0 1 1010,600"/>
    <path id="story-arc" d="M258,402 A395,395 0 1 0 942,402"/>
  </defs>

  <circle class="label-ring" cx="600" cy="600" r="480"/>

  <text class="wine-name">
    <textPath href="#title-arc" startOffset="50%" text-anchor="middle">Amber Moth Ridge</textPath>
  </text>

  <text class="vineyard-story">
    <textPath href="#story-arc" startOffset="50%" text-anchor="middle">Proximity to a river known by 9 different names along its flow, with the vineyard being situated near the area attributed to the 9th name.</textPath>
  </text>

  <circle class="label-artwork" cx="600" cy="600" r="345" fill="url(#marble-wash)"
          role="img" aria-label="Watercolour marbled river in pale blues with a line drawing of a damselfly at the top"/>

  <text class="brand-mark" x="600" y="735" text-anchor="middle">A/M</text>

  <text class="wine-style" x="600" y="800" text-anchor="middle">Full-Bodied</text>
  <text class="wine-type" x="600" y="845" text-anchor="middle">RED</text>
  <line class="craft-rule" x1="540" y1="855" x2="660" y2="855"/>
  <text class="craft-note" x="600" y="880" text-anchor="middle">HAND-CRAFTED</text>
</svg>
</body>
</html>
```